Velvo Cup - A jelly sugar free dessert.

We want to create 2 labels containing a packet of sugar-free jelly powder dessert. One product will be pineapple-flavored, and the other will have a cherry flavor. We want the product name to be "Velvo Cup," prominently displayed on the label, and as attractive as possible, along with the words "fără zahăr"(translated sugar-free) and the flavor of the fruit, respectively, pineapple and cherry. Additionally, we want "Doar 9 kcal per porție" to appear on the label as attractively as possible. We would like the layout to include an image of a female silhouette that is appealing (indicating that weight loss is possible through consumption of the respective product), and also should appear the words like "Cu aromă de ananas" (translation: with pineapple flavour) and "Cu aromă de cireșe" (translation: with cherry flavors). We also want an image of the prepared jelly, one in the color of pineapple and the other in the color of cherries, with fruits visible in the picture. Subsequently, the chosen winner will add the text provided by us with the company name, product description, ingredients, nutritional table, etc. The box will have the dimensions attached next to it according to the attached document. I am also attaching a picture of a sugar-free lemon-flavored jelly model, just to give you an idea, but it should meet our requirements. The colors should be attractive, suitable for a dessert.

Target Market(s)

people who want to loose weigh

Industry/Entity Type

food

Font styles to use
Serif
Sans Serif

Requirements
Must have
• Sugar-free words, woman body silhouette

```html
<!DOCTYPE html>
<html lang="ro">
<head>
<meta charset="utf-8">
<title>Velvo Cup – fără zahăr, cu aromă de ananas</title>
<link rel="stylesheet" href="https://fonts.googleapis.com/css2?family=Bangers&family=Kaushan+Script&family=Lobster&family=Ubuntu:wght@700&display=swap">
<style>
  :root {
    --stage: #e7e5d2;
    --sun-core: #fff7c4;
    --sun-mid: #fbd54a;
    --sun-edge: #f2a81d;
    --orange: #ef8a1c;
    --orange-deep: #e56b12;
    --red-orange: #d9462a;
    --brand: #d9542a;
    --white: #ffffff;
    --ink: #4a4a4a;
    --jelly-light: #ffe45c;
    --jelly-dark: #f0b400;
    --silhouette: #e4532b;
  }
  html, body {
    margin: 0;
    width: 1200px;
    height: 840px;
    overflow: hidden;
    background: var(--stage);
  }
  .label {
    position: absolute;
    left: 40px;
    top: 40px;
    width: 1120px;
    height: 760px;
    display: block;
  }
  .tagline { font-family: "Kaushan Script", cursive; fill: var(--red-orange); }
  .brand-name { font-family: "Lobster", cursive; fill: var(--brand); }
  .flavour { font-family: "Bangers", sans-serif; fill: var(--red-orange); letter-spacing: 2px; }
  .kcal-word { font-family: "Ubuntu", sans-serif; font-weight: 700; fill: var(--orange); }
  .kcal-number { font-family: "Ubuntu", sans-serif; font-weight: 700; fill: var(--white); }
  .kcal-unit { font-family: "Ubuntu", sans-serif; font-weight: 700; fill: var(--white); letter-spacing: 1px; }
  .copy { font-family: "Ubuntu", sans-serif; font-weight: 700; fill: var(--ink); letter-spacing: 0.5px; }
</style>
</head>
<body>
<svg class="label" viewBox="0 0 1120 760" xmlns="http://www.w3.org/2000/svg">
  <defs>
    <radialGradient id="sunburst" cx="0.45" cy="0.35" r="0.75">
      <stop offset="0" stop-color="var(--sun-core)"/>
      <stop offset="0.45" stop-color="var(--sun-mid)"/>
      <stop offset="1" stop-color="var(--sun-edge)"/>
    </radialGradient>
    <linearGradient id="jelly-tone" x1="0" y1="0" x2="1" y2="1">
      <stop offset="0" stop-color="var(--jelly-light)"/>
      <stop offset="1" stop-color="var(--jelly-dark)"/>
    </linearGradient>
    <linearGradient id="band-tone" x1="0" y1="0" x2="1" y2="0">
      <stop offset="0" stop-color="var(--orange-deep)"/>
      <stop offset="1" stop-color="var(--orange)"/>
    </linearGradient>
  </defs>

  <rect class="label-ground" width="1120" height="760" fill="url(#sunburst)"/>

  <!-- calorie corner -->
  <path class="kcal-corner-rim" d="M0 0 H270 Q250 250 0 350 Z" fill="var(--white)"/>
  <path class="kcal-corner" d="M0 0 H250 Q230 230 0 325 Z" fill="var(--orange)"/>
  <circle class="kcal-icon" cx="100" cy="100" r="42" fill="var(--white)"/>
  <text class="kcal-word" x="100" y="110" font-size="28" text-anchor="middle">kcal</text>
  <text class="kcal-number" x="100" y="200" font-size="62" text-anchor="middle">9</text>
  <text class="kcal-unit" x="100" y="228" font-size="16" text-anchor="middle">PER PORȚIE</text>

  <!-- prepared jelly with pineapple -->
  <g class="product-photo" role="img" aria-label="Photo of a yellow pineapple jelly dessert with a fresh pineapple and juice splash">
    <path d="M1120 0 H820 Q780 120 800 260 Q760 420 820 560 Q960 620 1120 580 Z" fill="url(#jelly-tone)"/>
  </g>

  <!-- headline -->
  <text class="tagline" x="560" y="118" font-size="44" text-anchor="middle">fără zahăr</text>
  <text class="brand-name" x="470" y="300" font-size="150" text-anchor="middle">Velvo Cup</text>
  <path class="brand-swash" d="M300 345 Q520 310 720 300" fill="none" stroke="var(--brand)" stroke-width="9" stroke-linecap="round"/>

  <!-- lower bands -->
  <path class="flavour-band" d="M0 470 Q520 560 1120 430 V760 H0 Z" fill="url(#band-tone)"/>
  <path class="copy-band" d="M0 650 Q560 640 1120 520 V760 H0 Z" fill="var(--white)"/>

  <g class="figure" role="img" aria-label="Orange silhouette of a slim dancing woman with raised arms">
    <rect x="150" y="380" width="170" height="380" rx="70" fill="var(--silhouette)"/>
  </g>

  <text class="flavour" x="360" y="600" font-size="84" transform="rotate(-10 360 600)">CU AROMĂ DE ANANAS!!</text>

  <g class="copy" transform="rotate(-9 430 700)" font-size="19">
    <text x="430" y="680">LOREM IPSUM DOLOR SIT AMET, CONSECTETUER ADIPISCING</text>
    <text x="430" y="706">ELIT. SED DIAM NONUMMY NIBH EUISMOD TINCIDUNT UT</text>
    <text x="430" y="732">LAOREET DOLORE MAGNA ALIQUAM ERAT VOLUTPAT. UT</text>
  </g>
</svg>
</body>
</html>
```